Sleek and Morden Business Card

Business Card Design for Business Name "Harbor Lantern Bureau (HLB)"
Offering Virtual Assistant (VA) services including Virtual Receptionist, Appointment and Diary Management. Taking and Answering calls for Sole Trader Businesses. Quotes, Invoices, Expense Reconciliation, Accounts Payable and Accounts Receivable.
Harbor Bureau offers clients the ease of a complete office without the physical need to having an office.
Target Market(s)
Target market are Sole Traders like Electricians, Plumbers, Painters etc.
Industry/Entity Type
Business
Colors
Designer to choose colors to be used in the design.
Look and feel
Each slider illustrates characteristics of the customer's brand and the style your logo design should communicate.

```html
<!DOCTYPE html>
<html lang="en">
<head>
<meta charset="utf-8">
<title>Harbor Lantern Bureau – Business Card</title>
<link rel="stylesheet" href="https://fonts.googleapis.com/css2?family=Open+Sans:wght@400;600;700;800&display=swap">
<style>
  :root {
    --brand-blue: #0a6fae;
    --brand-blue-deep: #065a96;
    --brand-blue-light: #0b9ad6;
    --ink: #3a3a3a;
    --muted: #666666;
    --paper: #ffffff;
    --band-dark: #0d0d0d;
    --band-mid: #2e2e2e;
  }
  * { box-sizing: border-box; margin: 0; padding: 0; }
  html, body {
    width: 900px; height: 1200px; overflow: hidden;
    background: var(--paper);
    font-family: "Open Sans", Arial, sans-serif;
  }
  .canvas { position: relative; width: 900px; height: 1200px; }

  .brand-header {
    position: absolute; top: 0; left: 0; width: 900px; height: 340px;
    background: var(--paper);
    display: flex; flex-direction: column; align-items: center; justify-content: center;
  }
  .wordmark {
    font-weight: 800; font-size: 100px; line-height: 1; letter-spacing: 2px;
    color: var(--brand-blue);
  }
  .wordmark-tagline {
    margin-top: 12px; font-size: 16px; letter-spacing: 1.2px; color: var(--ink);
  }

  .card-band {
    position: absolute; top: 340px; left: 0; width: 900px; height: 860px;
    background: linear-gradient(90deg, var(--band-dark) 0%, var(--band-mid) 100%);
  }
  .card {
    position: absolute; left: 170px; width: 560px; height: 311px;
  }
  .card-front { top: 89px; background: var(--paper); }
  .card-back {
    top: 460px;
    background: linear-gradient(135deg, var(--brand-blue-light) 0%, var(--brand-blue) 50%, var(--brand-blue-deep) 100%);
    display: flex; flex-direction: column; align-items: center; justify-content: center;
  }

  .card-front .card-logo {
    position: absolute; top: 56px; left: 0; width: 100%;
    display: flex; flex-direction: column; align-items: center;
  }
  .card-logo .wordmark { font-size: 68px; letter-spacing: 1px; }
  .card-logo .wordmark-tagline { margin-top: 5px; font-size: 12.5px; letter-spacing: 0.5px; }

  .card-back .wordmark { font-size: 93px; color: var(--paper); letter-spacing: 1px; }
  .card-back .wordmark-tagline { color: var(--paper); font-size: 17px; margin-top: 6px; letter-spacing: 0.8px; }

  .holder { position: absolute; left: 50px; top: 205px; }
  .holder-name { font-weight: 700; font-size: 19.5px; color: var(--brand-blue-deep); }
  .holder-role { font-size: 14.5px; color: var(--muted); margin-top: 2px; letter-spacing: 0.5px; }

  .contact {
    position: absolute; left: 272px; top: 202px;
    font-size: 14.5px; color: var(--muted); letter-spacing: 0.5px; line-height: 1.6;
  }
  .contact dt { display: inline-block; width: 65px; }
  .contact dd { display: inline; }
</style>
</head>
<body>
<main class="canvas">
  <header class="brand-header">
    <div class="wordmark">HLB</div>
    <div class="wordmark-tagline">Harbor Lantern Bureau</div>
  </header>

  <section class="card-band">
    <article class="card card-front">
      <div class="card-logo">
        <div class="wordmark">HLB</div>
        <div class="wordmark-tagline">Harbor Lantern Bureau</div>
      </div>
      <div class="holder">
        <div class="holder-name">Marla Quennel</div>
        <div class="holder-role">Owner</div>
      </div>
      <dl class="contact">
        <div><dt>Mobile:</dt><dd>0400 555 218</dd></div>
        <div><dt>Email&nbsp;&nbsp;:</dt><dd>marla@hlbureau.com.au</dd></div>
      </dl>
    </article>

    <article class="card card-back">
      <div class="wordmark">HLB</div>
      <div class="wordmark-tagline">Harbor Lantern Bureau</div>
    </article>
  </section>
</main>
</body>
</html>
```